Enterprise image desing

The designs are for a fashion store for young men and women.
Updates

Los diseƱos parecen similares

Target Market(s)

Young

Font styles to use
Sans Serif

Colors
ec1f27
ffffff
1b1b1b

Requirements
Must have
• Use clean and modern sources
Nice to have
• n / a
Should not have
• n / a

```html
<!DOCTYPE html>
<html lang="es">
<head>
<meta charset="utf-8">
<title>VELORA – Tarjetas de presentación</title>
<link href="https://fonts.googleapis.com/css2?family=Montserrat:wght@800&family=Arimo:wght@400;700&display=swap" rel="stylesheet">
<style>
  :root {
    --navy: #0f2d4d;
    --red: #ec1f27;
    --white: #ffffff;
    --ink: #1b2a44;
    --blush: #fbe5de;
    --mist: #d9d9df;
    --backdrop: #e9e7e4;
  }
  * { margin: 0; padding: 0; box-sizing: border-box; }
  html, body { width: 1200px; height: 997px; overflow: hidden; }
  body {
    background: var(--backdrop);
    position: relative;
    font-family: "Arimo", Arial, sans-serif;
  }
  .card {
    position: absolute;
    top: 344px;
    width: 540px;
    height: 309px;
    border-radius: 3px;
    overflow: hidden;
    box-shadow: 0 6px 18px rgba(0,0,0,0.12);
  }
  .card--back { left: 40px; background: var(--navy); color: var(--white); }
  .card--front { left: 620px; background: var(--white); color: var(--ink); }

  .brand {
    display: flex;
    align-items: center;
    gap: 9px;
    font-family: "Montserrat", Arial, sans-serif;
    font-weight: 800;
    letter-spacing: 1px;
  }
  .brand__mark { display: block; border-radius: 3px; }

  .card--back .brand {
    position: absolute;
    left: 0; right: 0; top: 112px;
    justify-content: center;
    font-size: 36px;
  }
  .card--back .brand__mark { width: 30px; height: 30px; background: var(--white); }
  .back-contact {
    position: absolute;
    left: 40px; bottom: 44px;
    font-size: 12.5px;
    line-height: 1.35;
  }

  .front-art { position: absolute; inset: 0; }
  .front-info { position: absolute; left: 30px; top: 38px; width: 300px; }
  .card--front .brand { font-size: 30px; color: var(--navy); }
  .card--front .brand__mark { width: 26px; height: 26px; background: var(--red); }
  .rule { height: 1.5px; background: var(--red); margin: 10px 0 8px; }
  .person__name { font-size: 16px; letter-spacing: 0.3px; }
  .person__role { font-size: 13.5px; font-weight: 700; }
  .address { font-size: 13px; line-height: 1.3; margin-bottom: 6px; }
  .contact-list { list-style: none; font-size: 13.5px; line-height: 1.4; }
  .contact-list li { display: flex; align-items: center; gap: 6px; }
  .contact-list svg { width: 13px; height: 13px; flex: none; }
</style>
</head>
<body>

<section class="card card--back" aria-label="Reverso de la tarjeta">
  <div class="brand"><span class="brand__mark"></span><span>VELORA</span></div>
  <p class="back-contact">
    Calle Olmedo e/ Sucre y Colón, Portovelo - Ecuador EC070301<br>
    (593)7 410-2287 | mruiz@velora.com.ec | www.velora.com.ec
  </p>
</section>

<section class="card card--front" aria-label="Anverso de la tarjeta">
  <svg class="front-art" viewBox="0 0 540 309" preserveAspectRatio="none" aria-hidden="true">
    <path d="M310 309 V70 Q310 0 380 0 H540 V309 Z" fill="var(--blush)"/>
    <path d="M460 309 V110 Q460 62 510 62 H540 V309 Z" fill="var(--white)"/>
    <path d="M478 309 V128 Q478 84 518 84 H540 V309 Z" fill="var(--mist)"/>
  </svg>

  <div class="front-info">
    <div class="brand"><span class="brand__mark"></span><span>VELORA</span></div>
    <div class="rule"></div>
    <p class="person__name">MATEO RUIZ ANDRADE</p>
    <p class="person__role">Gerente General</p>
    <div class="rule"></div>
    <p class="address">Calle Olmedo e/ Sucre y Colón,<br>Portovelo - Ecuador EC070301</p>
    <ul class="contact-list">
      <li>
        <svg viewBox="0 0 14 14"><circle cx="7" cy="7" r="6.2" fill="none" stroke="var(--red)" stroke-width="1.2"/><path d="M4.5 4 L6 4 L6.5 5.5 L5.7 6.2 Q6.6 7.8 7.9 8.4 L8.6 7.6 L10 8.1 L10 9.5 Q6 10 4.5 4 Z" fill="var(--red)"/></svg>
        (593)7 410-2287
      </li>
      <li>
        <svg viewBox="0 0 14 14"><circle cx="7" cy="7" r="6.2" fill="none" stroke="var(--red)" stroke-width="1.2"/><rect x="5" y="3.5" width="4" height="7" rx="0.8" fill="none" stroke="var(--red)" stroke-width="1"/></svg>
        (593) 98 517-3360
      </li>
      <li>
        <svg viewBox="0 0 14 14"><circle cx="7" cy="7" r="6.2" fill="none" stroke="var(--red)" stroke-width="1.2"/><rect x="4" y="4.8" width="6" height="4.4" fill="none" stroke="var(--red)" stroke-width="1"/><path d="M4 4.8 L7 7.2 L10 4.8" fill="none" stroke="var(--red)" stroke-width="1"/></svg>
        mruiz@velora.com.ec
      </li>
      <li>
        <svg viewBox="0 0 14 14"><circle cx="7" cy="7" r="6.2" fill="none" stroke="var(--red)" stroke-width="1.2"/><circle cx="7" cy="7" r="3.2" fill="none" stroke="var(--red)" stroke-width="1"/><path d="M3.8 7 H10.2 M7 3.8 Q5.4 7 7 10.2 M7 3.8 Q8.6 7 7 10.2" fill="none" stroke="var(--red)" stroke-width="0.8"/></svg>
        www.velora.com.ec
      </li>
    </ul>
  </div>
</section>

</body>
</html>
```